Zertifikat-Design für Bildungsträger im Bereich der Erwachsenenbildung
Zielgruppe
Talwerk Akademie - Zertifizierter Bildungsträger im Bereich der Erwachsenenbildung. Überwiegend Mitarbeiter in Unternehmen.
Aufgabenstellung
'Erstelle ein hochwertiges, modernes und exklusiv wirkendes Zertifikat für die Talwerk Akademie. Das Design soll professionell, minimalistisch und zugleich edel sein. Ziel ist es, ein Dokument zu gestalten, das den Eindruck vermittelt: 'Das ist das einzige und beste Zertifikat in der ganzen verdammten Welt.'
Das Zertifikat soll im Querformat (idealerweise DIN A4 horizontal) gestaltet werden. Der Inhalt soll zweisprachig (Deutsch und Englisch) dargestellt werden, klar gegliedert und typografisch hochwertig aufgebaut. Alle Inhalte sollten mittig ausgerichtet sein, mit gut erkennbarer visueller Hierarchie.
Der Haupttext lautet wie folgt:
'Talwerk Akademie gratuliert 'Name / Platzhalter' zum erfolgreichen Abschluss des Kurses 'Platzhalter' Datum, Unterschrift (siehe unten)
+englisch
'Talwerk Akademie hereby certifies that [Name of Participant / Placeholder] has successfully participated on 'date'.
Darunter sollen zwei stilisierte Unterschriften platziert werden – gerne von Hand gezeichnet oder elegant typografisch umgesetzt. Die Beschriftung unter den Unterschriften lautet: 'Leitung Talwerk Akademie'.
Ein zentrales Element ist das Hologramm. Muster das gelieferte Bild 'Hologramm.png'. Es muss deutlich sichtbar und hochwertig integriert werden. Die Aufschrift 'Talwerk' im Hologramm muss klar erkennbar sein. Idealer Platz wäre unten links oder rechts, eventuell mit einer leichten 3D-Anmutung oder Glanzeffekt.
Das gesamte Design muss der Corporate Identity der Talwerk Akademie entsprechen. Die verwendeten Farben sind: Hauptfarbe Dunkelblau (RGB 14, 32, 62), ergänzt durch Hellblau (RGB 241, 245, 250), ein zusätzliches Blau (RGB 65, 111, 174), Pink (RGB 140, 130, 227), Dunkellila (RGB 169, 97, 161), sowie Gelb (RGB 248, 216, 73) und Orange (RGB 220, 121, 70) für gezielte Akzente.
Als Schriftart ist ausschließlich Roboto zu verwenden. Der Name des Teilnehmers soll besonders hervorgehoben werden (z...

```html
<!DOCTYPE html>
<html lang="de">
<head>
<meta charset="utf-8">
<title>Talwerk Akademie – Zertifikat</title>
<link rel="stylesheet" href="https://fonts.googleapis.com/css2?family=Roboto:wght@300;400;500;700&display=swap">
<style>
  :root {
    --navy: #0e203e;
    --navy-mid: #1b325d;
    --blue: #3a6098;
    --light: #f1f5fa;
    --page: #e6e7eb;
    --white: #ffffff;
    --yellow: #f8d849;
    --holo-a: #dfe9f3;
    --holo-b: #8c82e3;
    --holo-c: #a961a1;
    --holo-d: #416fae;
  }
  * { box-sizing: border-box; margin: 0; padding: 0; }
  html, body {
    width: 1200px; height: 1200px; overflow: hidden;
    background: var(--page);
    font-family: "Roboto", sans-serif;
  }
  .certificate {
    position: absolute; left: 50px; top: 211px;
    width: 1100px; height: 778px;
    background: var(--light);
    box-shadow: 0 2px 8px rgba(14, 32, 62, 0.12);
  }
  .certificate-body {
    position: absolute; inset: 26px;
    background: linear-gradient(150deg, var(--blue) 0%, var(--navy-mid) 45%, var(--navy) 100%);
    color: var(--white);
  }
  .line {
    position: absolute; left: 0; right: 0; text-align: center;
  }
  .brand-name {
    top: 78px; font-weight: 500; font-size: 44px; line-height: 1.2;
    letter-spacing: 1px; color: var(--white);
  }
  .congrats { top: 222px; font-weight: 300; font-size: 31px; }
  .recipient {
    top: 272px; font-weight: 700; font-size: 55px; color: var(--yellow);
    letter-spacing: 0.5px;
  }
  .completion { top: 346px; font-weight: 300; font-size: 32px; line-height: 39px; }
  .issue-date { top: 445px; font-weight: 700; font-size: 23px; color: var(--yellow); letter-spacing: 0.5px; }
  .signatory {
    position: absolute; top: 540px; width: 200px;
    display: flex; flex-direction: column; align-items: center;
  }
  .signatory--director { left: 267px; }
  .signatory--lead { left: 532px; }
  .signature-area {
    width: 150px; height: 74px; border-radius: 4px;
    background: linear-gradient(180deg, rgba(255,255,255,0) 0%, rgba(255,255,255,0.08) 100%);
  }
  .signatory-name { font-size: 15px; font-weight: 400; margin-top: 6px; }
  .signatory-rule { width: 123px; height: 1.5px; background: var(--white); margin-top: 5px; }
  .signatory-role { font-size: 12px; font-weight: 500; margin-top: 7px; }
  .hologram-seal {
    position: absolute; left: 855px; top: 528px;
    width: 141px; height: 141px; border-radius: 5px;
    background:
      conic-gradient(from 20deg at 50% 50%, var(--holo-a), var(--white), var(--holo-d), var(--holo-a), var(--holo-b), var(--holo-c), var(--holo-a), var(--white), var(--holo-d), var(--holo-a));
    box-shadow: 0 4px 10px rgba(0, 0, 0, 0.35);
  }
</style>
</head>
<body>
  <main class="certificate">
    <section class="certificate-body">
      <p class="line brand-name">TALWERK AKADEMIE</p>

      <p class="line congrats">gratuliert /congratulates</p>
      <h1 class="line recipient">JONAS ELLERBROCK</h1>
      <p class="line completion">zum erfolgreichen Abschluss<br>on successfull completion</p>
      <p class="line issue-date">17-04-2025</p>

      <div class="signatory signatory--director">
        <div class="signature-area" role="img" aria-label="Handschriftliche Unterschrift der Direktorin"></div>
        <span class="signatory-name">Henrike v.d. Lohe</span>
        <span class="signatory-rule"></span>
        <span class="signatory-role">Direktorin</span>
      </div>

      <div class="signatory signatory--lead">
        <div class="signature-area" role="img" aria-label="Handschriftliche Unterschrift der Kursleitung"></div>
        <span class="signatory-name">Tobias Kranefeld</span>
        <span class="signatory-rule"></span>
        <span class="signatory-role">Kursleitung</span>
      </div>

      <div class="hologram-seal" role="img" aria-label="Hologramm-Siegel der Akademie"></div>
    </section>
  </main>
</body>
</html>
```